Business Journal Ad for a Commercial Real Estate Firm

I need to have an ad designed to be included in a business journal with a very short timeline (due 5/14/21). I can include the copies they came up with which I'm not a fan of. The ad size should be either: 4.875 x 6.125 OR 2.345 x 6.125. The content should include information on all three divisions of the company as shown in one of the example ads that are attached with the same contact information and company logos that are attached. You can view our company website at www.vellowbrookprop.com for additional information, photos, sample marketing, etc.

Target Market(s)

Business owners, creative, property owners, 35+

Industry/Entity Type

Real Estate

Requirements
Must have
• Graphics, color, green, company logo, contact info

```html
<!DOCTYPE html>
<html lang="en">
<head>
<meta charset="utf-8">
<title>Vellowbrook Real Estate – Journal Ad</title>
<link rel="stylesheet" href="https://fonts.googleapis.com/css2?family=Alice&family=Libre+Baskerville:wght@700&family=Mulish:wght@400;500;600&family=Dancing+Script:wght@500&display=swap">
<style>
  :root {
    --stage: #333333;
    --paper: #e9e6e0;
    --green: #11603a;
    --green-dark: #0a4a2b;
    --green-light: #1c7447;
    --gold: #ecd99a;
    --ink-green: #1b5732;
    --white: #ffffff;
  }
  * { margin: 0; padding: 0; box-sizing: border-box; }
  html, body { width: 1200px; height: 1200px; overflow: hidden; background: var(--stage); }
  .ad {
    position: absolute; left: 160px; top: 48px;
    width: 880px; height: 1104px;
    background: var(--paper);
    overflow: hidden;
  }
  .ad-shapes { position: absolute; inset: 0; width: 880px; height: 1104px; }
  .brand-mark {
    position: absolute; left: 37px; top: 47px;
    width: 164px; height: 164px; border-radius: 50%;
    background: var(--white);
  }
  .brand-name {
    position: absolute; left: 214px; top: 38px; width: 650px;
    text-align: center;
    font-family: "Alice", serif; color: var(--white);
    font-size: 92px; line-height: 1;
  }
  .brand-sub {
    position: absolute; left: 214px; top: 146px; width: 650px;
    text-align: center;
    font-family: "Alice", serif; color: var(--white);
    font-size: 44px; letter-spacing: 0.32em; line-height: 1;
  }
  .intro { position: absolute; left: 0; top: 310px; width: 880px; text-align: center; color: var(--ink-green); }
  .intro-headline { font-family: "Libre Baskerville", serif; font-weight: 700; font-size: 27px; line-height: 1.2; }
  .intro-body { font-family: "Mulish", sans-serif; font-size: 27px; line-height: 1.28; margin-top: 4px; }
  .intro-rule { width: 500px; margin: 12px auto 0; border-top: 2px dotted #8c9a8e; }
  .intro-script { font-family: "Dancing Script", cursive; font-weight: 500; font-size: 41px; line-height: 1.0; margin-top: 14px; }
  .division {
    position: absolute; top: 766px; width: 280px;
    text-align: center; color: var(--white);
  }
  .division-title {
    font-family: "Libre Baskerville", serif; font-weight: 700;
    color: var(--gold); font-size: 24px; line-height: 1.25;
  }
  .division-title span { text-decoration: underline; text-underline-offset: 4px; }
  .division-contact { font-family: "Mulish", sans-serif; font-weight: 500; font-size: 22px; line-height: 1.38; margin-top: 2px; }
  .division--sales { left: 14px; }
  .division--pm { left: 298px; }
  .division--homes { left: 584px; top: 774px; }
  .footer { position: absolute; left: 50px; top: 978px; color: var(--ink-green); font-family: "Mulish", sans-serif; }
  .footer-row { display: flex; align-items: center; gap: 10px; font-size: 19px; height: 29px; letter-spacing: 0.02em; }
  .footer-row svg { width: 20px; height: 20px; flex: none; }
  .footer-row--web { font-size: 29px; font-weight: 600; height: 36px; margin-top: 2px; letter-spacing: 0.01em; }
</style>
</head>
<body>
<div class="ad">
  <svg class="ad-shapes" viewBox="0 0 880 1104" aria-hidden="false">
    <defs>
      <linearGradient id="band" x1="0" y1="0" x2="1" y2="1">
        <stop offset="0" stop-color="#0c5131"/>
        <stop offset="0.5" stop-color="#177044"/>
        <stop offset="1" stop-color="#0c5131"/>
      </linearGradient>
      <linearGradient id="panel" x1="0" y1="0" x2="0" y2="1">
        <stop offset="0" stop-color="#157045"/>
        <stop offset="1" stop-color="#0b4d2d"/>
      </linearGradient>
      <linearGradient id="photo-city" x1="0" y1="0" x2="1" y2="1">
        <stop offset="0" stop-color="#8a7a68"/><stop offset="0.5" stop-color="#a45a3c"/><stop offset="1" stop-color="#5e6a56"/>
      </linearGradient>
      <linearGradient id="photo-tower" x1="0" y1="0" x2="0" y2="1">
        <stop offset="0" stop-color="#3f6ed0"/><stop offset="0.55" stop-color="#b7a2c4"/><stop offset="1" stop-color="#b9b09a"/>
      </linearGradient>
      <linearGradient id="photo-home" x1="0" y1="0" x2="1" y2="1">
        <stop offset="0" stop-color="#ddd5c6"/><stop offset="0.6" stop-color="#c9bca6"/><stop offset="1" stop-color="#5c7a48"/>
      </linearGradient>
    </defs>

    <path class="header-band" fill="url(#band)"
      d="M17 16 H862 V222 C760 206 680 224 560 250 C430 278 330 300 200 292 C120 287 60 282 17 285 Z"/>

    <path class="division-panel" fill="url(#panel)" d="M20 644 H288 V954 C220 948 150 928 90 924 C60 922 38 924 20 927 Z"/>
    <path class="division-panel" fill="url(#panel)" d="M305 644 H572 V950 C500 960 420 962 305 955 Z"/>
    <path class="division-panel" fill="url(#panel)" d="M590 644 H859 V965 H590 Z"/>

    <g class="division-photo">
      <circle cx="151" cy="644" r="114" fill="var(--white)"/>
      <circle cx="151" cy="644" r="98" fill="none" stroke="#7f8a5e" stroke-width="4"/>
      <circle cx="151" cy="644" r="92" fill="url(#photo-city)" role="img" aria-label="Aerial photo of downtown brick commercial buildings"/>
    </g>
    <g class="division-photo">
      <circle cx="438" cy="644" r="114" fill="var(--white)"/>
      <circle cx="438" cy="644" r="98" fill="none" stroke="#7f8a5e" stroke-width="4"/>
      <circle cx="438" cy="644" r="92" fill="url(#photo-tower)" role="img" aria-label="Photo of a managed office building at dusk"/>
    </g>
    <g class="division-photo">
      <circle cx="726" cy="644" r="114" fill="var(--white)"/>
      <circle cx="726" cy="644" r="98" fill="none" stroke="#7f8a5e" stroke-width="4"/>
      <circle cx="726" cy="644" r="92" fill="url(#photo-home)" role="img" aria-label="Photo of a residential home porch with shrubs"/>
    </g>

    <line x1="470" y1="1053" x2="745" y2="1053" stroke="var(--ink-green)" stroke-width="2"/>
    <circle class="social-dot" cx="768" cy="1053" r="24" fill="var(--green)"/>
    <circle class="social-dot" cx="827" cy="1053" r="24" fill="var(--green)"/>
  </svg>

  <div class="brand-mark"></div>
  <div class="brand-name">Vellowbrook</div>
  <div class="brand-sub">REAL ESTATE</div>

  <div class="intro">
    <p class="intro-headline">FOR EXPERTISE &amp; EXPERIENCE BEYOND COMPARE</p>
    <p class="intro-body">contact Vellowbrook’s divisions for Commercial,<br>Homes and Property Management.</p>
    <div class="intro-rule"></div>
    <p class="intro-script">Impacting Ashford and surrounding areas<br>for over 10 years.</p>
  </div>

  <div class="division division--sales">
    <p class="division-title">COMMERCIAL<br><span>SALES</span></p>
    <p class="division-contact">555.201.4410<br>VellowbrookRE.com</p>
  </div>
  <div class="division division--pm">
    <p class="division-title">COMMERCIAL<br><span>PROPERTY MGMNT</span></p>
    <p class="division-contact">555.201.4420<br>VellowbrookPM.com</p>
  </div>
  <div class="division division--homes">
    <p class="division-title">RESIDENTIAL<br><span>HOMES</span></p>
    <p class="division-contact">555.201.4430<br>VellowbrookHomes.com</p>
  </div>

  <div class="footer">
    <div class="footer-row">
      <svg viewBox="0 0 24 24"><path fill="var(--ink-green)" d="M6.6 10.8a15.2 15.2 0 0 0 6.6 6.6l2.2-2.2a1 1 0 0 1 1-.25 11.4 11.4 0 0 0 3.6.57 1 1 0 0 1 1 1V20a1 1 0 0 1-1 1A17 17 0 0 1 3 4a1 1 0 0 1 1-1h3.5a1 1 0 0 1 1 1c0 1.25.2 2.45.57 3.57a1 1 0 0 1-.25 1z"/></svg>
      <span>555.201.4410</span>
    </div>
    <div class="footer-row">
      <svg viewBox="0 0 24 24"><path fill="var(--ink-green)" d="M12 2a7 7 0 0 0-7 7c0 5.2 7 13 7 13s7-7.8 7-13a7 7 0 0 0-7-7zm0 9.5A2.5 2.5 0 1 1 12 6.5a2.5 2.5 0 0 1 0 5z"/></svg>
      <span>48 LINDEN HOLLOW RD., ASHFORD, NC 28000</span>
    </div>
    <div class="footer-row footer-row--web">
      <svg viewBox="0 0 24 24"><g fill="none" stroke="var(--ink-green)" stroke-width="2"><circle cx="12" cy="12" r="9"/><ellipse cx="12" cy="12" rx="4" ry="9"/><path d="M3 12h18"/></g></svg>
      <span>www.vellowbrookprop.com</span>
    </div>
  </div>
</div>
</body>
</html>
```